The First Annual Tamsworth Legacy Supper

Something similar to the attached but an attention grabber. It needs to attract people with money to spend!

```html
<!DOCTYPE html>
<html lang="en">
<head>
<meta charset="utf-8">
<title>The First Annual Tamsworth Legacy Supper</title>
<link href="https://fonts.googleapis.com/css2?family=Bebas+Neue&family=Archivo:wght@400;600;800;900&display=swap" rel="stylesheet">
<style>
:root{
  --blue:#7fa3d9;
  --blue-deep:#6b92cf;
  --ink:#333336;
  --dark:#3a3a3c;
  --band:#ececec;
  --page:#58585a;
  --white:#ffffff;
  --grey-tag:#e2e2e2;
}
*{margin:0;padding:0;box-sizing:border-box}
html,body{width:1200px;height:2853px;overflow:hidden;background:var(--page)}
body{position:relative;font-family:"Archivo",Arial,sans-serif;color:var(--ink)}
.flyer{position:absolute;left:100px;top:720px;width:1000px;height:1414px;background:var(--white);overflow:hidden;box-shadow:0 10px 30px rgba(0,0,0,.35)}
.abs{position:absolute}
.hero-photo{left:0;top:0;width:1000px;height:675px;background:linear-gradient(180deg,#7fa3d9 0%,#8fb1e0 30%,#c7d8ee 55%,#e9eef4 66%,#d6dde4 78%,#9aa276 90%,#7a8a4c 100%)}
.presenter{top:40px;width:100%;text-align:center;color:var(--white);font-size:19px;letter-spacing:.3px}
.title{top:86px;width:100%;text-align:center;color:var(--white);font-family:"Bebas Neue",Impact,sans-serif;font-size:116px;line-height:89px;letter-spacing:1px}
.date{left:42px;top:694px;width:312px;white-space:nowrap;color:var(--blue);font-weight:900;font-size:60px;line-height:66px}
.rule{height:2px;background:var(--blue)}
.start-time{left:46px;top:778px;font-weight:800;font-size:26px;line-height:30px;color:var(--ink);white-space:nowrap}
.year-tag{left:362px;top:709px;width:56px;height:139px;background:var(--grey-tag);display:flex;align-items:center;justify-content:center}
.year-tag span{transform:rotate(-90deg);color:var(--white);font-weight:900;font-size:48px;letter-spacing:1px}
.divider{left:446px;top:709px;width:2px;height:139px;background:var(--blue)}
.highlights{left:470px;top:724px;color:var(--blue);font-weight:900;font-size:38px;line-height:43px;white-space:nowrap}
.intro{left:40px;top:884px;width:432px;font-size:16.5px;line-height:22px;text-align:justify;color:var(--ink)}
.intro p{margin-bottom:12px}
.ticket-box{left:504px;top:891px;width:454px;height:227px;border:2px solid var(--blue);border-radius:12px;overflow:hidden;text-align:center}
.ticket-head{background:var(--blue);color:var(--white);height:111px;padding-top:8px}
.ticket-head small{display:block;font-size:18px}
.ticket-head strong{display:block;font-weight:800;font-size:32px;line-height:35px}
.ticket-body{padding-top:10px;font-size:18.5px;line-height:24px}
.ticket-body .donor{color:var(--blue)}
.outlets{left:0;top:1167px;width:1000px;height:109px;background:var(--band);border-top:3px solid var(--blue)}
.outlets-tab{left:284px;top:1164px;width:415px;height:36px;background:var(--blue);border-radius:0 0 28px 28px;color:var(--white);font-weight:600;font-size:24px;line-height:36px;text-align:center}
.outlet{top:1216px;display:flex;gap:10px;white-space:nowrap}
.outlet svg{margin-top:4px;flex:none}
.outlet b{display:block;font-weight:600;font-size:17.5px;line-height:24px}
.outlet span{display:block;font-size:14px;line-height:20px}
.outlet-sep{top:1214px;width:1px;height:46px;background:#b9b9b9}
.contact-band{left:0;top:1276px;width:1000px;height:138px;background:var(--dark)}
.follow{left:37px;top:1278px;width:457px;height:111px;background:var(--blue);border-radius:14px;display:flex;align-items:center;padding-left:20px;gap:18px;overflow:hidden}
.follow .mark{width:72px;height:72px;border-radius:12px;background:var(--white);flex:none}
.follow p{color:var(--white);font-weight:800;font-size:18px;line-height:25px;white-space:nowrap}
.alt-heading{left:540px;top:1294px;color:var(--white);font-weight:800;font-size:19px}
.phone{top:1334px;display:flex;gap:14px;color:var(--white);white-space:nowrap}
.phone svg{flex:none}
.phone b{display:block;font-weight:800;font-size:18px;line-height:21px}
.phone span{display:block;font-size:18px;line-height:21px}
</style>
</head>
<body>
<main class="flyer">
  <div class="abs hero-photo" role="img" aria-label="Photograph of the long white community hall with a pale metal roof under a blue sky with clouds"></div>
  <p class="abs presenter">THE TAMSWORTH COMMUNITY CENTER PRESENTS</p>
  <h1 class="abs title">THE FIRST ANNUAL<br>TAMSWORTH LEGACY<br>SUPPER</h1>

  <p class="abs date">APRIL 23</p>
  <div class="abs rule" style="left:40px;top:767px;width:310px"></div>
  <p class="abs start-time">STARTING AT 5:00 PM<br>WITH COCKTAIL HOUR</p>
  <div class="abs rule" style="left:40px;top:846px;width:310px"></div>
  <div class="abs year-tag"><span>2022</span></div>
  <div class="abs divider"></div>
  <p class="abs highlights">LIVE AUCTION, SILENT<br>AUCTION, RAFFLE AND<br>A CASH BAR!</p>

  <div class="abs intro">
    <p>Come on out to the Tamsworth Community Center for a delicious prime rib dinner, drinks, entertainment and more! There will be plenty of amazing auction items for everyone to choose from.</p>
    <p>All proceeds will go to the Tamsworth Community Center. We will share some history of the school and each year we will highlight a local family. This year will be the Harlow family who have been here for ....years!!</p>
    <p>High Side Barn, dirt bike, custom knives, a pack trip and so much more!</p>
  </div>

  <section class="abs ticket-box">
    <div class="ticket-head">
      <small>TICKETS FOR THE EVENT ARE</small>
      <strong>$50 EACH OR<br>$90 FOR A COUPLE</strong>
    </div>
    <div class="ticket-body">
      <p>Tickets For The 10x12 High Side Barn<br>$25 Each Or 5 For $100.</p>
      <p class="donor">Donated By: Ridgeline Shed Works Of<br>Carrow Falls, Value $6500</p>
    </div>
  </section>

  <div class="abs outlets"></div>
  <div class="abs outlets-tab">GET YOUR TICKETS FROM</div>
  <div class="abs outlet" style="left:40px">
    <svg width="18" height="24" viewBox="0 0 18 24"><path d="M9 0a9 9 0 0 0-9 9c0 6.5 9 15 9 15s9-8.5 9-15a9 9 0 0 0-9-9z" fill="#7fa3d9"/><circle cx="9" cy="9" r="3.5" fill="#ececec"/></svg>
    <div><b>Ridgeline Shed Works in Carrow Falls</b><span>18 Alder Way, Carrow Falls</span></div>
  </div>
  <div class="abs outlet-sep" style="left:400px"></div>
  <div class="abs outlet" style="left:417px">
    <svg width="18" height="24" viewBox="0 0 18 24"><path d="M9 0a9 9 0 0 0-9 9c0 6.5 9 15 9 15s9-8.5 9-15a9 9 0 0 0-9-9z" fill="#7fa3d9"/><circle cx="9" cy="9" r="3.5" fill="#ececec"/></svg>
    <div><b>Summit Peak Realty</b><span>42 W Cedar St, Carrow Falls</span></div>
  </div>
  <div class="abs outlet-sep" style="left:718px"></div>
  <div class="abs outlet" style="left:740px">
    <svg width="18" height="24" viewBox="0 0 18 24"><path d="M9 0a9 9 0 0 0-9 9c0 6.5 9 15 9 15s9-8.5 9-15a9 9 0 0 0-9-9z" fill="#7fa3d9"/><circle cx="9" cy="9" r="3.5" fill="#ececec"/></svg>
    <div><b>Tamsworth Store</b><span>310 County Road 9, Tamsworth</span></div>
  </div>

  <div class="abs contact-band"></div>
  <div class="abs follow">
    <div class="mark"></div>
    <p>Follow the Tamsworth Community<br>Center's online page to see<br>all the auction items available!</p>
  </div>
  <p class="abs alt-heading">OR GET THEM FROM</p>
  <div class="abs phone" style="left:548px">
    <svg width="36" height="40" viewBox="0 0 36 40"><rect width="36" height="40" rx="6" fill="#7fa3d9"/><path d="M13 9c-2 1-4 3-3 7 1 5 5 11 10 14 3 2 5 1 7-1l-4-5-3 2c-2-1-5-6-5-8l3-2z" fill="#fff"/></svg>
    <div><b>MARLA JENNET</b><span>(555) 014-2231</span></div>
  </div>
  <div class="abs phone" style="left:766px">
    <svg width="36" height="40" viewBox="0 0 36 40"><rect width="36" height="40" rx="6" fill="#7fa3d9"/><path d="M13 9c-2 1-4 3-3 7 1 5 5 11 10 14 3 2 5 1 7-1l-4-5-3 2c-2-1-5-6-5-8l3-2z" fill="#fff"/></svg>
    <div><b>CORRINE ASHBY</b><span>(555) 019-7746</span></div>
  </div>
</main>
</body>
</html>
```